Lanternfield Drinks business cards

We need a business card design for our new logo. The company is modern, progressive, professional, yet approachable. The key products are ready to drink bottles and cans of coffee based beverages.
These cards will be a critical part of the first impression made by our sales organization, business development team, and all external facing personnel.
Card can be a vertical or horizontal orientation.

Target Market(s)

Customers, suppliers, business partners

Industry/Entity Type

Business

Contact Information for Business Card

Business cards should feature Company Name and Logo.

Font styles to use
Serif

Colors

Designer to choose colors to be used in the design.

Requirements
Must have
• Strong readability of Name, phone #, mobile number and email address.
• Job title, website url, Street Address, and other details can be secondary level readability.
Nice to have
• High impact, simplistic quality design.
• Ok to utilize the 'H in the box' separate from the company name

```html
<!DOCTYPE html>
<html lang="en">
<head>
<meta charset="utf-8">
<title>Lanternfield Drinks — Business Cards</title>
<link href="https://fonts.googleapis.com/css2?family=Cinzel:wght@400;700&family=Open+Sans:wght@400&display=swap" rel="stylesheet">
<style>
  :root{
    --backdrop:#3a3a3c;
    --card:#1e1e1f;
    --stripe-light:#2b2b2c;
    --stripe-dark:#151516;
    --accent:#e8582a;
    --ink:#ffffff;
  }
  *{margin:0;padding:0;box-sizing:border-box}
  html,body{width:1200px;height:900px;overflow:hidden;background:var(--backdrop)}
  .canvas{position:relative;width:1200px;height:900px}
  .card{position:absolute;width:640px;height:366px;border-radius:18px;overflow:hidden;background:var(--card);box-shadow:0 14px 30px rgba(0,0,0,.45)}
  .card--front{left:70px;top:70px}
  .card--back{left:490px;top:464px}
  .card__art{position:absolute;inset:0;width:100%;height:100%}
  .holder{position:absolute;left:180px;top:66px}
  .holder__name{font-family:"Cinzel",serif;font-size:27px;color:var(--ink);letter-spacing:1px}
  .holder__title{font-family:"Cinzel",serif;font-size:14px;color:var(--accent);letter-spacing:1px;margin-top:2px}
  .holder__rule{width:104px;height:3px;background:var(--accent);margin-top:14px}
  .contacts{position:absolute;left:150px;top:200px;list-style:none;font-family:"Open Sans",sans-serif;font-size:15px;color:var(--ink)}
  .contacts li{display:flex;align-items:center;gap:10px;height:27px}
  .contacts svg{width:15px;height:15px;fill:var(--accent)}
  .brand{display:flex;align-items:center;gap:10px;font-family:"Cinzel",serif;font-weight:700;color:var(--accent);white-space:nowrap}
  .brand__mark{flex:none;border:3px solid var(--accent)}
  .brand--small{position:absolute;right:130px;bottom:46px;font-size:14px;gap:8px}
  .brand--small .brand__mark{width:32px;height:32px}
  .brand--large{position:absolute;left:0;right:0;top:150px;justify-content:center;font-size:29px}
  .brand--large .brand__mark{width:52px;height:52px}
</style>
</head>
<body>
<main class="canvas">

  <section class="card card--front" aria-label="Card front">
    <svg class="card__art" viewBox="0 0 640 366" preserveAspectRatio="none" aria-hidden="true">
      <rect x="28" y="0" width="26" height="366" fill="var(--stripe-light)"/>
      <rect x="54" y="0" width="26" height="366" fill="var(--stripe-dark)"/>
      <rect x="80" y="0" width="28" height="366" fill="var(--stripe-light)"/>
      <rect x="532" y="0" width="28" height="366" fill="var(--stripe-light)"/>
      <rect x="560" y="0" width="26" height="366" fill="var(--stripe-dark)"/>
      <rect x="586" y="0" width="26" height="366" fill="var(--stripe-light)"/>
      <path d="M0 0H640V36H548L528 20H112L92 36H0Z" fill="var(--accent)"/>
      <path d="M0 366H640V330H548L528 346H112L92 330H0Z" fill="var(--accent)"/>
    </svg>
    <div class="holder">
      <p class="holder__name">Your Name</p>
      <p class="holder__title">Job Title</p>
      <div class="holder__rule"></div>
    </div>
    <ul class="contacts">
      <li><svg viewBox="0 0 24 24"><path d="M6.6 10.8a15 15 0 0 0 6.6 6.6l2.2-2.2c.3-.3.7-.4 1-.2 1.1.4 2.3.6 3.6.6.6 0 1 .4 1 1V20c0 .6-.4 1-1 1A17 17 0 0 1 3 4c0-.6.4-1 1-1h3.5c.6 0 1 .4 1 1 0 1.3.2 2.5.6 3.6.1.3 0 .7-.2 1z"/></svg>+971 XXXXXXX</li>
      <li><svg viewBox="0 0 24 24"><path d="M2 5h20v14H2zM4 7l8 6 8-6v-.1H4z"/></svg>x@y.com</li>
      <li><svg viewBox="0 0 24 24"><path d="M12 2a7 7 0 0 0-7 7c0 5 7 13 7 13s7-8 7-13a7 7 0 0 0-7-7zm0 9.5A2.5 2.5 0 1 1 12 6.5a2.5 2.5 0 0 1 0 5z"/></svg>your address here</li>
    </ul>
    <div class="brand brand--small">
      <span class="brand__mark"></span><span class="brand__name">Lanternfield Drinks</span>
    </div>
  </section>

  <section class="card card--back" aria-label="Card back">
    <svg class="card__art" viewBox="0 0 640 366" preserveAspectRatio="none" aria-hidden="true">
      <rect x="28" y="0" width="26" height="366" fill="var(--stripe-light)"/>
      <rect x="54" y="0" width="26" height="366" fill="var(--stripe-dark)"/>
      <rect x="80" y="0" width="28" height="366" fill="var(--stripe-light)"/>
      <rect x="532" y="0" width="28" height="366" fill="var(--stripe-light)"/>
      <rect x="560" y="0" width="26" height="366" fill="var(--stripe-dark)"/>
      <rect x="586" y="0" width="26" height="366" fill="var(--stripe-light)"/>
      <rect x="210" y="88" width="220" height="190" fill="#1a1a1b"/>
      <path d="M0 0H640V36H548L528 20H112L92 36H0Z" fill="var(--accent)"/>
      <path d="M0 366H640V330H548L528 346H112L92 330H0Z" fill="var(--accent)"/>
    </svg>
    <div class="brand brand--large">
      <span class="brand__mark"></span><span class="brand__name">Lanternfield Drinks</span>
    </div>
  </section>

</main>
</body>
</html>
```